I would like a Buisness card and matching letterhead for my small but personal hobby/buisness.
Something elegant, professional and pretty.
I mainly do wedding cakes in our small rural area. But also do occasion cakes, cupcakes, cookies and catering events.
I am thinking something subtle, vintage, scrolls, lace, damask, nothing too wow or out there. But open to any suggestions.

Catering

Simply Sugared Crumb
abn: 53 418 907 245
Marlene Fosbury
Wattlebrook
t: 0491 305 862
e: simplysugaredcrumb@mailbakery.example

Simply Sugared Crumb

Wordmark Logo
• Elegance and class
• Should not have Hearts or Bows

```html
<!DOCTYPE html>
<html lang="en">
<head>
<meta charset="utf-8">
<title>Simply Sugared Crumb – Business Card</title>
<link rel="stylesheet" href="https://fonts.googleapis.com/css2?family=Josefin+Sans:wght@300;400&display=swap">
<style>
  :root {
    --page-bg: #ece8e6;
    --card-pink: #f3bfdd;
    --ink-brown: #5b2c2f;
    --scroll-tone: #d99cbf;
  }
  html, body {
    margin: 0;
    padding: 0;
    width: 1200px;
    height: 1000px;
    overflow: hidden;
    background: var(--page-bg);
  }
  .canvas {
    position: relative;
    width: 1200px;
    height: 1000px;
  }
  .business-card {
    position: absolute;
    left: 150px;
    top: 225px;
    width: 900px;
    height: 550px;
    background: var(--card-pink);
    box-shadow: 0 6px 18px rgba(60, 30, 40, 0.18);
    font-family: "Josefin Sans", sans-serif;
    color: var(--ink-brown);
    text-align: center;
  }
  .scroll-ornament {
    position: absolute;
    left: 50%;
    transform: translateX(-50%);
    background: linear-gradient(90deg, rgba(217,156,191,0), var(--scroll-tone) 20%, var(--scroll-tone) 80%, rgba(217,156,191,0));
    border-radius: 20px;
  }
  .scroll-top { top: 150px; width: 420px; height: 34px; }
  .scroll-bottom { top: 268px; width: 440px; height: 40px; }
  .wordmark {
    position: absolute;
    top: 195px;
    left: 0;
    right: 0;
    margin: 0;
    font-weight: 300;
    font-size: 36px;
    letter-spacing: 3px;
    text-transform: uppercase;
  }
  .owner-line {
    position: absolute;
    top: 240px;
    left: 0;
    right: 0;
    margin: 0;
    font-weight: 400;
    font-size: 17px;
    letter-spacing: 2px;
  }
  .contact-details {
    position: absolute;
    top: 340px;
    left: 0;
    right: 0;
    margin: 0;
    font-weight: 400;
    font-size: 16px;
    letter-spacing: 1.5px;
    line-height: 34px;
  }
  .contact-details span + span { margin-left: 18px; }
</style>
</head>
<body>
  <div class="canvas">
    <article class="business-card">
      <div class="scroll-ornament scroll-top" role="img" aria-label="Vintage filigree scroll flourish above the business name"></div>
      <h1 class="wordmark">Simply Sugared Crumb</h1>
      <p class="owner-line">Marlene Fosbury Wattlebrook</p>
      <div class="scroll-ornament scroll-bottom" role="img" aria-label="Vintage filigree scroll flourish below the owner name"></div>
      <p class="contact-details">
        <span>abn: 53 418 907 245</span><span>t: 0491 305 862</span><br>
        <span>e: simplysugaredcrumb@mailbakery.example</span>
      </p>
    </article>
  </div>
</body>
</html>
```